Fresh-Up our Master Presentation

We are looking for someone who can revise our main presentation and make it more attractive. The previous layout and the slides are uploaded here and need to be revised. You are welcome to work with icons etc. here. The goal is to make it look a little more creative and modern. Brisk Otter is a company from the creative industry and therefore it would be great if it also shows this.

Target Market(s)

B2B

Industry/Entity Type

Communication and Content Creation

Font styles to use
Sans Serif

```html
<!DOCTYPE html>
<html lang="de">
<head>
<meta charset="utf-8">
<title>Brisk Otter – Master Presentation</title>
<link rel="stylesheet" href="https://fonts.googleapis.com/css2?family=Poppins:wght@600;700&family=Inter:wght@400;500;600;700&display=swap">
<style>
:root{
  --navy:#2f3d5c;
  --navy-deep:#26324d;
  --orange:#d4552f;
  --grey:#8e8e8e;
  --light:#e1e0e3;
  --white:#ffffff;
  --ink:#2b2b35;
  --brown:#5b3b34;
  --pill:#4a5775;
}
*{box-sizing:border-box;margin:0;padding:0}
html,body{width:1200px;height:2803px;overflow:hidden}
body{background:var(--light);font-family:Inter,Arial,sans-serif;color:var(--ink);position:relative}
.slide{position:absolute;width:540px;height:304px;background:var(--white);overflow:hidden}
.abs{position:absolute}
.photo{position:absolute}
.h{font-family:Poppins,Arial,sans-serif;font-weight:600;color:var(--navy);line-height:1.1}
.rule{position:absolute;height:3px;width:48px;background:var(--orange)}
.logo{position:absolute;display:flex;align-items:center;gap:4px;font-family:Poppins,Arial,sans-serif;font-weight:600;font-size:11px;color:var(--navy)}
.logo i{display:block;width:15px;height:15px;border-radius:50%;background:currentColor}
.logo.light{color:var(--white)}
.foot{position:absolute;right:16px;bottom:15px;display:flex;align-items:center;gap:8px;font-size:6px;letter-spacing:1px;color:var(--grey)}
.foot b{display:flex;width:11px;height:11px;border-radius:50%;background:var(--navy);color:#fff;font-size:6px;align-items:center;justify-content:center;letter-spacing:0}
.foot.on-navy b{background:#fff;color:var(--navy)}
.bullets{position:absolute;list-style:none;font-size:7px;line-height:1.25;color:var(--ink)}
.bullets li{position:relative;padding-left:13px;margin-bottom:6px}
.bullets li:before{content:"";position:absolute;left:2px;top:3px;width:3px;height:3px;border-radius:50%;background:var(--orange)}

.cover{position:absolute;width:880px;height:496px;overflow:hidden;transform-origin:0 0}
.cover .stage{position:absolute;left:0;top:0;width:880px;height:458px;background:radial-gradient(ellipse at 72% 30%,#7b86a0 0%,#4a5778 35%,var(--navy) 75%)}
.cover .logo{left:70px;top:72px;font-size:34px;gap:10px}
.cover .logo i{width:52px;height:52px}
.cover .title{position:absolute;left:67px;top:178px;font-family:Poppins,Arial,sans-serif;font-weight:700;font-size:47px;line-height:1.18;color:#fff}
.cover .rule{left:70px;top:300px;width:82px;height:4px}
.cover .sub{position:absolute;left:71px;top:318px;font-size:17px;letter-spacing:2px;color:#fff}
.cover .date{position:absolute;left:71px;top:394px;font-size:11px;letter-spacing:2px;font-weight:600;color:#fff}
.cover .band{position:absolute;left:0;top:458px;width:880px;height:38px;background:#fff;text-align:center;line-height:38px;font-size:11px;letter-spacing:2.5px;color:var(--ink)}
.cover.pale .stage{background:linear-gradient(90deg,#f5f6f8 0%,#eef0f4 35%,#b8bfcd 65%,#8e98ae 100%)}
.cover.pale .logo,.cover.pale .title{color:var(--navy)}
.cover.pale .sub{color:var(--orange)}
.cover.pale .date{color:var(--navy)}
.cover.pale .band{background:var(--navy);color:#fff}

.stat{position:absolute;display:flex;align-items:center;gap:10px;font-size:6.5px;color:#fff}
.stat span.ic{width:14px;height:14px;border:1.2px solid #fff;border-radius:4px;flex:none}
.note{position:absolute;background:var(--pill);border-radius:4px;color:#fff;font-size:4.5px;text-align:center;padding:3px 6px;line-height:1.3}
.phone{position:absolute;border-radius:12px;border:3px solid #f1f1f3;box-shadow:0 0 0 1px #c9cbd2}

.iconrow{position:absolute;left:33px;display:flex;align-items:center;gap:8px;font-size:6px;line-height:1.25;width:210px}
.iconrow i{flex:none;width:18px;height:18px;border-radius:50%;border:1.5px solid var(--navy)}

.card{position:absolute;top:110px;width:148px;height:146px;border-radius:9px;color:#fff;font-size:6px;text-align:center;line-height:1.3;padding:50px 14px 0}
.card .q{position:absolute;left:12px;top:-12px;width:34px;height:34px;border-radius:50%;display:flex;align-items:center;justify-content:center;font-family:Poppins,Arial,sans-serif;font-weight:700;font-size:26px;line-height:1;padding-top:12px;border:3px solid #fff}
.card .tab{position:absolute;left:58px;top:-12px;width:60px;height:24px;border-radius:8px 8px 0 0;background:#f0f0f2}
.card strong{display:block;margin-top:12px;font-size:5.5px;letter-spacing:.3px}

.price{position:absolute;left:28px;top:102px;width:488px;border-collapse:collapse;font-size:7px}
.price th{background:var(--navy);color:#fff;text-align:left;padding:2px 4px;font-weight:700}
.price td{padding:2px 4px;border-bottom:1px solid #c9ccd4;color:var(--ink)}
.price td:first-child{color:var(--navy);font-weight:700}
.price tr:nth-child(odd) td{background:#eceef2}
</style>
</head>
<body>

<div class="cover" style="left:160px;top:83px">
  <div class="stage" role="img" aria-label="Konzertbühne mit Moderatoren vor jubelndem Publikum und Rauch"></div>
  <div class="logo light"><i></i>Brisk Otter</div>
  <div class="title">Presentation<br>Title Goes Here</div>
  <div class="rule"></div>
  <div class="sub">Sub Title of Presentation Goes Here</div>
  <div class="date">Sunday, May 21, 2023</div>
  <div class="band">Copyright © 2023 Brisk Otter.</div>
</div>

<div class="cover" style="left:51px;top:836px;transform:scale(.6136)">
  <div class="stage" role="img" aria-label="Konzertbühne mit Moderatoren vor jubelndem Publikum"></div>
  <div class="logo light"><i></i>Brisk Otter</div>
  <div class="title">Presentation<br>Title Goes Here</div>
  <div class="rule"></div>
  <div class="sub">Sub Title of Presentation Goes Here</div>
  <div class="date">Sunday, May 21, 2023</div>
  <div class="band">Copyright © 2023 Brisk Otter.</div>
</div>
<div class="cover pale" style="left:609px;top:836px;transform:scale(.6136)">
  <div class="stage" role="img" aria-label="Helle, verblassende Konzertbühne mit Publikum"></div>
  <div class="logo"><i></i>Brisk Otter</div>
  <div class="title">Presentation<br>Title Goes Here</div>
  <div class="rule"></div>
  <div class="sub">Sub Title of Presentation Goes Here</div>
  <div class="date">Sunday, May 21, 2023</div>
  <div class="band">Copyright © 2023 Brisk Otter.</div>
</div>

<section class="slide" style="left:51px;top:1157px">
  <div class="abs" style="left:0;top:0;width:237px;height:304px;background:var(--navy)"></div>
  <div class="photo" style="left:34px;top:34px;width:250px;height:215px;background:linear-gradient(160deg,#c4cbd6,#8a8f99 55%,#3a3d45)" role="img" aria-label="Porträt der beiden Moderatoren vor einer Altstadtkulisse"></div>
  <h2 class="h abs" style="left:312px;top:48px;font-size:20px">Jonas Keller und<br>Marco Brunner</h2>
  <div class="rule" style="left:312px;top:103px;width:36px"></div>
  <ul class="bullets" style="left:310px;top:122px;width:200px">
    <li>Moderatoren, Podcaster, Social Media Hosts und DJs: Jonas Keller und Marco Brunner sind schweizweit bekannte Persönlichkeiten mit hohem Unterhaltungswert.</li>
    <li>Jonas Keller moderiert seit 20 Jahren und Marco Brunner seit 10 Jahren Morgensendungen, insbesondere von Radio Pulse in der Schweiz. Als Morgenduo «Keller und Brunner», mit dem Podcast «Das Sofagespräch» und mit verschiedenen Social Media-Formaten wie «Erst Feierabend, wenn…» haben sie sich eine grosse Community aufgebaut.</li>
  </ul>
  <div class="logo light" style="left:16px;top:276px"><i></i>Brisk Otter</div>
  <div class="foot"><span>Copyright © 2023 Brisk Otter.</span><b>3</b></div>
</section>

<section class="slide" style="left:609px;top:1157px">
  <h2 class="h abs" style="left:30px;top:22px;font-size:20px">Social Media-Präsenz</h2>
  <div class="rule" style="left:30px;top:52px;width:50px"></div>
  <div class="abs" style="left:0;top:108px;width:540px;height:136px;background:var(--navy)"></div>
  <div class="phone" style="left:22px;top:80px;width:80px;height:168px;background:linear-gradient(180deg,#9aa0a8,#c98b2e 60%,#b7771f)" role="img" aria-label="Smartphone mit Foto eines Moderators in gelber Jacke"></div>
  <div class="h abs" style="left:118px;top:91px;font-size:10px">Jonas Keller</div>
  <div class="stat" style="left:120px;top:120px"><span class="ic"></span>Pixgram: 48'700 Follower</div>
  <div class="stat" style="left:120px;top:145px"><span class="ic"></span>Friendbook: 29'200 Follower</div>
  <div class="stat" style="left:120px;top:170px"><span class="ic"></span>Posts zu den Themen<br>Unterhaltung, Sport, Familie</div>
  <div class="note" style="left:120px;top:202px;width:128px">Auf Pixgram erreichte Konten pro Monat: 78'900 | Erreichte Zielgruppe: 53% Frauen / 46% Männer</div>
  <div class="phone" style="left:272px;top:80px;width:80px;height:168px;background:linear-gradient(180deg,#8c6a4f,#2e2f33 60%,#1e1f22)" role="img" aria-label="Smartphone mit Foto eines Moderators in dunkler Jacke"></div>
  <div class="h abs" style="left:368px;top:91px;font-size:10px">Marco Brunner</div>
  <div class="stat" style="left:368px;top:120px"><span class="ic"></span>Pixgram: 63'700 Follower</div>
  <div class="stat" style="left:368px;top:145px"><span class="ic"></span>Friendbook: 29'200 Follower</div>
  <div class="stat" style="left:368px;top:170px"><span class="ic"></span>Posts zu den Themen<br>Unterhaltung, Motorrad, Sport</div>
  <div class="note" style="left:368px;top:202px;width:128px">Auf Pixgram erreichte Konten pro Monat: 140'600 | Erreichte Zielgruppe: 56% Frauen / 43% Männer</div>
  <div class="logo" style="left:16px;top:276px"><i></i>Brisk Otter</div>
  <div class="foot"><span>Copyright © 2023 Brisk Otter.</span><b>4</b></div>
</section>

<section class="slide" style="left:51px;top:1478px">
  <div class="abs" style="left:303px;top:35px;width:237px;height:269px;background:var(--navy)"></div>
  <div class="photo" style="left:270px;top:35px;width:240px;height:214px;background:linear-gradient(160deg,#3a3f9a,#6c3aa8 45%,#1c2250)" role="img" aria-label="Live-Podcast auf einer Bühne vor grossem Publikum"></div>
  <h2 class="h abs" style="left:35px;top:45px;font-size:20px">Der Podcast</h2>
  <div class="rule" style="left:35px;top:76px;width:46px"></div>
  <div class="iconrow" style="top:94px"><i></i>«Das Sofagespräch» gehört zu den Top 10-Podcasts auf Soundwave (Soundwave-Charts 2022) und ist der erfolgreichste Comedy Podcast der Schweiz.</div>
  <div class="iconrow" style="top:124px"><i></i>Seit 2019 sind über 200 Folgen des Podcasts erschienen. Sie wurden über 8 Millionen Mal gestreamt.</div>
  <div class="iconrow" style="top:150px"><i></i>Jede Folge wird von durchschnittlich 50'000 Menschen angehört!</div>
  <div class="iconrow" style="top:174px"><i></i>Der Podcast wurde bereits zwei Mal live vor jeweils 1'200 «Zuhörer*innen» aufgezeichnet. Die beiden Shows waren in wenigen Sekunden restlos ausverkauft.</div>
  <div class="iconrow" style="top:204px"><i></i>Zum Podcast gehört eine Pixgram Seite mit fast 24'000 Abonnent*innen.</div>
  <div class="logo" style="left:16px;top:276px"><i></i>Brisk Otter</div>
  <div class="foot on-navy" style="color:#d7dbe3"><span>Copyright © 2023 Brisk Otter.</span><b>5</b></div>
</section>

<section class="slide" style="left:609px;top:1478px">
  <div class="abs" style="left:0;top:0;width:540px;height:187px;background:var(--navy)"></div>
  <h2 class="h abs" style="left:35px;top:24px;font-size:20px;color:#fff">Vidtube-Content</h2>
  <div class="rule" style="left:35px;top:54px;width:46px"></div>
  <div class="photo" style="left:27px;top:88px;width:149px;height:75px;background:linear-gradient(135deg,#e9e1d6,#c9a27a 60%,#d3c2a8)" role="img" aria-label="Videovorschau mit zwei Moderatoren an einem Tisch"></div>
  <div class="abs" style="left:190px;top:68px;width:164px;height:104px;border-radius:5px;background:#1a1d22;padding:4px">
    <div class="photo" style="position:relative;width:100%;height:100%;background:linear-gradient(180deg,#7fb4e6,#4fa6d6 55%,#2d87b8)" role="img" aria-label="Videovorschau mit Sprung in einen Pool"></div>
  </div>
  <div class="abs" style="left:176px;top:172px;width:192px;height:6px;border-radius:0 0 4px 4px;background:#c8cad0"></div>
  <div class="photo" style="left:364px;top:88px;width:148px;height:75px;background:linear-gradient(180deg,#111 0%,#2b2f38 30%,#5c6576 70%,#111)" role="img" aria-label="Videovorschau einer Mundart-Sendung"></div>
  <p class="abs" style="left:32px;top:208px;width:480px;font-size:7.5px;line-height:1.3">Seit vielen Jahren sind Jonas Keller und Marco Brunner mit höchst erfolgreichen Vidtube-Formaten wie «Erst Feierabend, wenn…», «Remo &amp; Sämi» oder «Mundart für Anfänger» präsent. Ihr Vidtube Channel hat über 17'000 Abonnent*innen! Jonas Keller und Marco Brunner gewannen 2022 zusammen mit dem Social Team von Pulse Events den «Alpine Comedy Award».</p>
  <div class="logo" style="left:16px;top:276px"><i></i>Brisk Otter</div>
  <div class="foot"><span>Copyright © 2023 Brisk Otter.</span><b>6</b></div>
</section>

<section class="slide" style="left:51px;top:1800px">
  <div class="photo" style="left:349px;top:0;width:191px;height:304px;background:linear-gradient(160deg,#3b2a7a,#7a3a8e 40%,#2a2f5e 75%,#1b1d3a)" role="img" aria-label="Unscharfes Bühnenfoto mit Lichtern"></div>
  <h2 class="h abs" style="left:30px;top:22px;font-size:20px">Starker Content</h2>
  <div class="rule" style="left:30px;top:52px;width:46px"></div>
  <p class="abs" style="left:30px;top:72px;width:290px;font-size:7.5px;line-height:1.3">«Uns ist es wichtig, dass wir Kooperationen mit Organisationen und Brands eingehen, welche zu uns passen. Wir haben über Jahre eine treue und loyale Community aufgebaut und das geht nur über guten und authentischen Content.»</p>
  <div class="abs" style="left:30px;top:124px;font-size:7px;font-weight:700;color:var(--brown)">Jonas Keller &amp; Marco Brunner</div>
  <div class="abs" style="left:0;top:148px;width:444px;height:108px;background:var(--brown)"></div>
  <div class="photo" style="left:29px;top:161px;width:82px;height:83px;background:linear-gradient(135deg,#9a9a9a,#c33a35 50%,#8a8a8a)" role="img" aria-label="Rotes Auto von oben"></div>
  <div class="photo" style="left:122px;top:161px;width:82px;height:83px;background:linear-gradient(135deg,#2f4fc2,#e4e6ee 55%,#3040a8)" role="img" aria-label="Moderator mit Kind"></div>
  <div class="photo" style="left:215px;top:161px;width:82px;height:83px;background:linear-gradient(180deg,#4d6a44,#dfe5e8 50%,#6b746b)" role="img" aria-label="Wasserfall in den Bergen"></div>
  <div class="photo" style="left:307px;top:161px;width:82px;height:83px;background:linear-gradient(135deg,#e6e8ea,#c02a2a 50%,#3b3b3b)" role="img" aria-label="Rennmotorrad in Schräglage"></div>
  <div class="logo" style="left:16px;top:276px"><i></i>Brisk Otter</div>
  <div class="foot" style="color:#e3d6de"><span>Copyright © 2023 Brisk Otter.</span><b>7</b></div>
</section>

<section class="slide" style="left:609px;top:1800px">
  <div class="abs" style="left:0;top:0;width:237px;height:304px;background:var(--navy)"></div>
  <div class="photo" style="left:35px;top:35px;width:250px;height:214px;background:radial-gradient(ellipse at 30% 40%,#f0822e 0%,#a0331f 25%,#2a2230 60%,#141419)" role="img" aria-label="DJ-Auftritt mit Flammensäulen vor Publikum"></div>
  <h2 class="h abs" style="left:312px;top:46px;font-size:20px">Moderationen und<br>DJ-Auftritte</h2>
  <div class="rule" style="left:312px;top:98px;width:36px"></div>
  <ul class="bullets" style="left:310px;top:120px;width:200px">
    <li>Jonas Keller und Marco Brunner sind jedes Jahr an unzähligen Events als DJs und / oder Moderatoren präsent. Sie profitieren hierbei von ihrer langen Erfahrung als Radio und TV-Moderatoren.</li>
    <li>Auch im Rahmen der Pulse Events treten Jonas Keller und Marco Brunner regelmässig vor bis zu 50'000 Menschen auf.</li>
    <li>Als DJs spielen Sie ein breites Hit-Repertoire. Sie präsentieren eigene Partyserien wie zum Beispiel in Kooperation mit Pulse im «Kulturhalle Nord» und im «Dachsaal in Aarwil».</li>
  </ul>
  <div class="logo light" style="left:16px;top:276px"><i></i>Brisk Otter</div>
  <div class="foot"><span>Copyright © 2023 Brisk Otter.</span><b>8</b></div>
</section>

<section class="slide" style="left:51px;top:2122px">
  <h2 class="h abs" style="left:30px;top:22px;font-size:20px">Individuelle Folien</h2>
  <div class="rule" style="left:30px;top:52px;width:46px"></div>
  <div class="abs" style="left:0;top:75px;width:540px;height:1px;background:#e4e5e8"></div>
  <div class="abs" style="left:100px;top:72px;width:7px;height:7px;border-radius:50%;background:#cfd1d6"></div>
  <div class="abs" style="left:267px;top:72px;width:7px;height:7px;border-radius:50%;background:#cfd1d6"></div>
  <div class="abs" style="left:434px;top:72px;width:7px;height:7px;border-radius:50%;background:#cfd1d6"></div>
  <div class="card" style="left:29px;background:var(--navy)"><span class="tab"></span><span class="q" style="background:var(--navy)">”</span>Phasellus eget commodo arcu. Nunc vitae semper dui. Integer venenatis, tellus sit amet interdum pretium, erat neque rhoncus turpis, a aliquam augue ligula eget erat. Nunc placerat, arcu nec mattis fermentum, nisi mauris convallis nunc, ut luctus nunc nisl id ex. Nam semper tristique mauris.<strong>NAME GOES HERE</strong></div>
  <div class="card" style="left:197px;background:var(--orange)"><span class="tab"></span><span class="q" style="background:var(--orange)">”</span>Phasellus eget commodo arcu. Nunc vitae semper dui. Integer venenatis, tellus sit amet interdum pretium, erat neque rhoncus turpis, a aliquam augue ligula eget erat. Nunc placerat, arcu nec mattis fermentum, nisi mauris convallis nunc, ut luctus nunc nisl id ex. Nam semper tristique mauris.<strong>NAME GOES HERE</strong></div>
  <div class="card" style="left:364px;background:var(--grey)"><span class="tab"></span><span class="q" style="background:var(--grey)">”</span>Phasellus eget commodo arcu. Nunc vitae semper dui. Integer venenatis, tellus sit amet interdum pretium, erat neque rhoncus turpis, a aliquam augue ligula eget erat. Nunc placerat, arcu nec mattis fermentum, nisi mauris convallis nunc, ut luctus nunc nisl id ex. Nam semper tristique mauris.<strong>NAME GOES HERE</strong></div>
  <div class="logo" style="left:16px;top:276px"><i></i>Brisk Otter</div>
  <div class="foot"><span>Copyright © 2023 Brisk Otter.</span><b>9</b></div>
</section>

<section class="slide" style="left:609px;top:2122px">
  <h2 class="h abs" style="left:30px;top:22px;font-size:20px">Leistungen Social Media</h2>
  <div class="rule" style="left:30px;top:52px;width:46px"></div>
  <p class="abs" style="left:30px;top:82px;font-size:7.5px">Social-Media Umsetzungen werden grundsätzlich wie folgt kalkuliert:</p>
  <table class="price">
    <tr><th>Post</th><th>Keller</th><th>Brunner</th><th>Keller &amp; Brunner</th></tr>
    <tr><td>Stories</td><td>CHF 2'600</td><td>CHF 3'300</td><td>CHF 5'400</td></tr>
    <tr><td>Foto und einfache Videoposts</td><td>CHF 3'900</td><td>CHF 4'900</td><td>CHF 7'900</td></tr>
    <tr><td>Umfängliche Reels</td><td>CHF 5'900</td><td>CHF 6'900</td><td>CHF 9'900</td></tr>
  </table>
  <p class="abs" style="left:30px;top:172px;font-size:8.5px">Zusätzliche Reichweite über Plattformen von Pulse Events: auf Anfrage möglich.</p>
  <ul class="abs" style="left:30px;top:190px;list-style:none;font-size:5.5px;line-height:1.75;color:var(--grey)">
    <li><span style="color:var(--orange)">•</span> Preise inkl. Kreation und Produktion, exkl. MWST.</li>
    <li><span style="color:var(--orange)">•</span> Branchenexklusivität: Zuzüglich 50% des Gesamtvolumens.</li>
    <li><span style="color:var(--orange)">•</span> Buyouts: 50% pro Content Piece.</li>
    <li><span style="color:var(--orange)">•</span> Rabatt bei Abschluss einer weiteren Vereinbarung für 2024: 20% auf das Gesamtvolumen.</li>
  </ul>
  <div class="logo" style="left:16px;top:276px"><i></i>Brisk Otter</div>
  <div class="foot"><span>Copyright © 2023 Brisk Otter.</span><b>10</b></div>
</section>

<section class="slide" style="left:330px;top:2443px;background:var(--navy)">
  <div class="photo" style="left:0;top:0;width:540px;height:280px;background:linear-gradient(90deg,var(--navy) 0%,var(--navy) 38%,#56617c 70%,#3d4864)" role="img" aria-label="Live-Podcast-Bühne mit zwei Moderatoren"></div>
  <div class="photo" style="left:45px;top:46px;width:73px;height:73px;border-radius:50%;background:linear-gradient(180deg,#c9ccd2,#7e848f);border:2px solid #fff" role="img" aria-label="Porträt der Ansprechperson"></div>
  <div class="logo light" style="left:44px;top:134px;font-size:14px;gap:6px"><i style="width:20px;height:20px"></i>Brisk Otter</div>
  <div class="abs" style="left:44px;top:170px;font-size:8px;font-weight:700;color:#fff">Ich freue mich auf die Zusammenarbeit.</div>
  <div class="abs" style="left:44px;top:195px;display:flex;flex-direction:column;gap:7px;font-size:7px;color:#fff">
    <div style="display:flex;gap:8px;align-items:center"><svg width="9" height="9" viewBox="0 0 10 10"><path d="M2 1l2 2-1 1.5c.7 1.3 1.3 1.9 2.5 2.5L7 6l2 2-1.3 1.5C4.5 9 1 5.5.6 2.3z" fill="none" stroke="#fff" stroke-width="1"/></svg>+41 79 555 01 23</div>
    <div style="display:flex;gap:8px;align-items:center"><svg width="9" height="9" viewBox="0 0 10 10"><circle cx="5" cy="5" r="4" fill="none" stroke="#fff"/><circle cx="5" cy="5" r="1.6" fill="none" stroke="#fff"/></svg>lena@briskotter.ch</div>
    <div style="display:flex;gap:8px;align-items:center"><svg width="9" height="9" viewBox="0 0 10 10"><circle cx="5" cy="5" r="4" fill="none" stroke="#fff"/><path d="M1 5h8M5 1c-2 2.5-2 5.5 0 8M5 1c2 2.5 2 5.5 0 8" fill="none" stroke="#fff" stroke-width=".8"/></svg>https://www.briskotter.ch</div>
  </div>
  <div class="abs" style="left:0;top:280px;width:540px;height:24px;background:#fff;text-align:center;line-height:24px;font-size:6px;letter-spacing:1.5px;color:var(--ink)">Copyright © 2023 Brisk Otter.</div>
</section>

</body>
</html>
```